Here's your chance to make lots of children happy! Colourful and fun bag design for candies

Happy New Year 2019 to all you creative souls out there! It's time to create a design that would bring happiness to a lot of children, big and small, all around the world! We are updating our packaging to make it more colourful, attractive/cute and fun. This assignment is for a series of 5 designs for 5 different candy flavours - Coconut HARD Candy (with Western Australian Sea Salt), Coconut CHEWY candy, Cola, Mint, and Tamarind. The general look of the 5 packaging must be similar. To differentiate, please use different colours, product name (the above 5 flavours) and pictures representing the flavours. As you can see, from our old packaging, the designs are very fragmented. The front dimension of the bag is 145mm wide and 205mm height, including sealing area: Top seal - 25mm, bottom seal 15mm. Our parent logo is SunKite and appears on the top left. You may or may not include an open window to show the wrapped candies inside, depending on your design. Please see attached files for our old designs. You may use the included draft template as a guide, you may choose to use our old pictures or new ones. A couple of our latest packaging series are also attached. Other products can be found on our website - www.velortaq.com.my. Please do not use large areas of white or black as much as possible in your design.

Target Market(s)

Target audience - children for mint and cola, adults for coconut and tamarind

Font styles to use
Sans Serif

Requirements
Should not have
• Large blocks of white or black

```html
<!DOCTYPE html>
<html lang="en">
<head>
<meta charset="utf-8">
<title>SunKite Candy Bags</title>
<link href="https://fonts.googleapis.com/css2?family=Fredoka:wght@500;600;700&display=swap" rel="stylesheet">
<style>
  :root {
    --page: #ffffff;
    --cola-red: #e8312a;
    --cola-red-dark: #c81f1a;
    --cola-seal: #d92a23;
    --cola-shadow: #8f1410;
    --tam-yellow: #f3b21c;
    --tam-orange: #f08a1c;
    --tam-seal: #f2a11e;
    --tam-shadow: #a85a10;
    --white: #ffffff;
    --candy-gold: #f0a23a;
    --candy-gold-dark: #9a4e12;
    --tam-beige: #e9d3b5;
    --tam-brown: #5a3a1e;
    --tam-purple: #9a3fc0;
    --tam-purple-dark: #4d1c66;
    --logo-dark: #3a1a14;
  }
  * { box-sizing: border-box; margin: 0; padding: 0; }
  html, body { width: 1200px; height: 1200px; overflow: hidden; background: var(--page); }
  .canvas { position: relative; width: 1200px; height: 1200px; font-family: "Fredoka", sans-serif; }

  .bag {
    position: absolute; top: 374px; width: 444px; height: 646px; overflow: hidden;
    box-shadow: 0 18px 30px rgba(0,0,0,0.18);
  }
  .bag--cola { left: 172px;
    background: repeating-linear-gradient(90deg, var(--cola-red) 0 37px, var(--cola-red-dark) 37px 74px); }
  .bag--tamarind { left: 647px;
    background: repeating-linear-gradient(90deg, var(--tam-yellow) 0 37px, var(--tam-orange) 37px 74px); }

  .seal { position: absolute; left: 0; right: 0; height: 62px; z-index: 1; }
  .seal--top { top: 0; }
  .seal--bottom { bottom: 0; }
  .bag--cola .seal { background: repeating-linear-gradient(180deg, var(--cola-seal) 0 4px, var(--cola-red-dark) 4px 8px); }
  .bag--tamarind .seal { background: repeating-linear-gradient(180deg, var(--tam-seal) 0 4px, var(--tam-orange) 4px 8px); }

  .brand {
    position: absolute; left: 12px; top: 84px; z-index: 3; display: flex; align-items: center; gap: 5px;
    background: var(--logo-dark); color: var(--white); padding: 3px 8px 3px 4px;
    font-weight: 600; font-size: 17px; letter-spacing: 0.5px;
  }
  .brand-mark { width: 16px; height: 16px; background: var(--white); }

  .photo-disc { position: absolute; border-radius: 50%; background: var(--white); z-index: 1; }
  .photo { position: absolute; border-radius: 50%; z-index: 2; }
  .bag--cola .photo-disc { left: 118px; top: 205px; width: 280px; height: 280px; }
  .bag--cola .photo { left: 88px; top: 222px; width: 240px; height: 200px;
    background: radial-gradient(ellipse at 55% 50%, #9a4614 0, #6b2410 55%, rgba(232,49,42,0) 72%); }
  .bag--tamarind .photo-disc { left: 83px; top: 150px; width: 284px; height: 284px; }
  .bag--tamarind .photo { left: 70px; top: 140px; width: 280px; height: 230px;
    background: radial-gradient(ellipse at 50% 50%, #c7ab8a 0, #9a865a 55%, rgba(243,178,28,0) 72%); }

  .tagline-stack {
    position: absolute; left: 222px; top: 112px; z-index: 4; color: var(--white);
    font-weight: 600; font-size: 30px; line-height: 1.05; text-shadow: 0 2px 3px var(--cola-shadow);
  }
  .tagline-stack .amp { font-size: 22px; display: block; }

  .product-name { position: absolute; left: 0; right: 0; z-index: 4; text-align: center; font-weight: 700; line-height: 1; }
  .cola-word { top: 360px; font-size: 104px; color: var(--white);
    -webkit-text-stroke: 3px var(--cola-red-dark); text-shadow: 0 6px 0 var(--cola-shadow); letter-spacing: -2px; }
  .cola-candy { top: 452px; font-size: 60px; color: var(--candy-gold); text-shadow: 0 4px 0 var(--candy-gold-dark); transform: rotate(-3deg); }
  .tam-word { top: 362px; font-size: 70px; color: var(--tam-beige); text-shadow: 0 5px 0 var(--tam-brown); letter-spacing: -1px; }
  .tam-candy { top: 432px; font-size: 60px; color: var(--tam-purple); text-shadow: 0 4px 0 var(--tam-purple-dark); transform: rotate(-3deg); }
  .tam-tagline { position: absolute; left: 0; right: 0; top: 508px; z-index: 4; text-align: center; color: var(--white);
    font-weight: 600; font-size: 30px; text-shadow: 0 2px 3px var(--tam-shadow); }
</style>
</head>
<body>
<main class="canvas">
  <section class="bag bag--cola">
    <div class="seal seal--top"></div>
    <div class="brand"><span class="brand-mark"></span>SunKite</div>
    <div class="photo-disc"></div>
    <div class="photo" role="img" aria-label="Glass of cola splashing with scattered cola candies"></div>
    <p class="tagline-stack">Fizzy<span class="amp">&amp;</span>Refreshing</p>
    <h2 class="product-name cola-word">COLA</h2>
    <p class="product-name cola-candy">CANDY</p>
    <div class="seal seal--bottom"></div>
  </section>

  <section class="bag bag--tamarind">
    <div class="seal seal--top"></div>
    <div class="brand"><span class="brand-mark"></span>SunKite</div>
    <div class="photo-disc"></div>
    <div class="photo" role="img" aria-label="Tamarind pods with leaves and scattered tamarind candies"></div>
    <h2 class="product-name tam-word">TAMARIND</h2>
    <p class="product-name tam-candy">CANDY</p>
    <p class="tam-tagline">Sweet, Sour &amp; Salt</p>
    <div class="seal seal--bottom"></div>
  </section>
</main>
</body>
</html>
```